Door Hanger Design for Electricians Serving Homes

I would like our logo incorporated into the door hanger. We would like a place for a tear off section on the bottom of the hanger with our contact information: K&T Electric - (555) 318-4702 - www.kandtelectric.example - info@kandtelectric.example.
Door Hanger Script
Front Side of the Door Hanger:
[Company Logo]
Need a Reliable Electrician?
Your Local Electrical Expert is Just Around the Corner!
• Quick Response Times
• Affordable Rates
• Quality Workmanship
• Fully Licensed & Insured
• Special Offer:
• 10% OFF Your First Service Call!
Back Side of the Door Hanger:
Don't Let Electrical Issues Keep You in the Dark!
From flickering lights to complete system upgrades, we've got all your
residential electrical needs covered. Our services include:
• Electrical Repairs & Troubleshooting
• Lighting Installation & Upgrades
• Safety Inspections & Code Compliance
• Energy-Efficient Solutions
• 24/7 Emergency Services
• Why Choose Us?
• Friendly, Local Service
• Over 30 Years of Experience
• Satisfaction Guaranteed
• Upfront Pricing
Call Us Today: [Your Phone Number]
Visit Our Website: [Your Website]
Book Your Appointment Now and Claim Your 10% Discount!
Offer valid for new customers on the first visit only. Mention this door hanger when
booking.
[Your Company Name and Contact Information]
Follow Us on Social Media for More Tips and Special Offers!
[Icons for social media platforms: Chatterpage, Pixmosaic, Quibbler, etc.]
Design Tips:
Use bold, clear fonts for easy reading.
Incorporate your brand colors and logo for instant recognition.
Include a clear call to action (CTA) on both sides.
Add a tear-off section at the bottom with your contact information for
convenience.
Use high-quality images or graphics related to electrical work to catch
the eye.
This door hanger design and copy aim to attract residential clients by
highlighting the benefits of your electrical services, special offers, and
how they can easily get in touch with you for their electrical needs.
The door knocker template will have three of the same design on front and three of the same design on the back. This template is from the print shop.

```html
<!DOCTYPE html>
<html lang="en">
<head>
<meta charset="utf-8">
<title>K&amp;T Electric Door Hanger</title>
<link href="https://fonts.googleapis.com/css2?family=Poppins:wght@400;500;600;700;800&family=League+Gothic&display=swap" rel="stylesheet">
<style>
:root{
  --red:#ec1c24;
  --ink:#0d0d0d;
  --white:#ffffff;
  --stage:#7f7f7f;
  --paper:#f4f4f4;
}
*{box-sizing:border-box;margin:0;padding:0}
html,body{width:1200px;height:1117px;overflow:hidden;background:var(--stage)}
body{position:relative;font-family:"Poppins",sans-serif;color:var(--ink)}
.hanger{position:absolute;top:46px;width:445px;height:1024px;overflow:hidden;background:var(--paper)}
.hanger--front{left:151px}
.hanger--back{left:638px}
.hanger__art{position:absolute;inset:0}
.abs{position:absolute}
.center{left:0;right:0;text-align:center}

/* logo */
.logo{position:absolute;left:113px;top:327px;width:216px;height:216px;border-radius:50%;background:var(--white);display:flex;flex-direction:column;align-items:center;justify-content:center;padding-top:24px}
.logo__name{font-weight:800;font-size:62px;line-height:1;color:var(--ink);letter-spacing:-1px}
.logo__sub{font-weight:800;font-size:19px;color:var(--ink);margin-top:10px;letter-spacing:.5px}

.front-kicker{top:526px;font-size:18px;font-weight:500}
.front-title{top:552px;font-size:31px;font-weight:800;line-height:31px;letter-spacing:-.3px}
.front-title .red{color:var(--red)}

.perks{position:absolute;left:28px;top:662px;width:389px;height:128px;border:2px solid var(--red);background:var(--white)}
.perk{position:absolute;font-size:18px;line-height:18px;padding-left:22px}
.tick{position:absolute;left:0;top:2px;width:13px;height:13px}

.offer-line{position:absolute;left:28px;top:808px;width:389px;height:3px;background:var(--red)}
.offer-pill{position:absolute;left:130px;top:812px;width:184px;height:30px;border-radius:15px;background:var(--red);color:var(--white);font-weight:700;font-size:20px;text-align:center;line-height:30px;z-index:2}
.offer-box{position:absolute;left:43px;top:842px;width:359px;height:53px;background:var(--white);display:flex;align-items:center;justify-content:center;gap:14px;font-family:"League Gothic",sans-serif;white-space:nowrap}
.offer-pct{color:var(--red);font-size:50px;line-height:1;display:flex;align-items:center}
.offer-pct small{display:flex;flex-direction:column;font-size:20px;line-height:16px;margin-left:2px}
.offer-text{font-size:35px;line-height:1;color:var(--ink);margin-top:8px}

.tear{position:absolute;left:0;right:0;top:914px;border-top:1.5px dashed #cfcfcf}
.foot{position:absolute;color:var(--white);font-size:15px;line-height:16px;white-space:nowrap}
.foot b{font-weight:700}
.foot-ico{position:absolute;width:14px;height:14px}

/* back */
.back-title{top:320px;font-size:27px;font-weight:800;line-height:28px;letter-spacing:-.3px}
.back-title .red{color:var(--red)}
.back-lede{top:380px;font-size:14.5px;line-height:16.5px;padding:0 44px}
.info{position:absolute;left:36px;top:447px;width:372px;height:213px}
.info__frame{position:absolute;left:184px;top:0;right:0;bottom:0;border:2px solid var(--red);border-left:none}
.info__frame::before{content:"";position:absolute;left:0;top:0;bottom:0;width:2px;background:var(--red)}
.info__base{position:absolute;left:0;right:0;bottom:0;height:2px;background:var(--red)}
.info__tab{position:absolute;left:0;top:0;width:186px;height:28px;background:var(--red);border-radius:14px 0 0 14px;color:var(--white);font-weight:700;font-size:18px;padding-left:22px;line-height:28px}
.info__head{position:absolute;left:206px;top:30px;font-weight:800;font-size:18px}
.info__head .red{color:var(--red)}
.item{position:absolute;font-size:12px;line-height:14px;padding-left:17px;white-space:nowrap}
.item .tick{width:9px;height:9px;top:2px}

.call{top:682px;font-size:16px}
.call b{font-size:22px;font-weight:700}
.site-label{top:718px;font-size:15px}
.site{top:734px;font-size:21px;font-weight:700}
.social{position:absolute;left:38px;top:771px;width:368px;height:26px;border-radius:13px;background:var(--red);color:var(--white);font-weight:700;font-size:10px;line-height:26px;padding-left:14px;white-space:nowrap}
.social__dots{position:absolute;right:16px;top:8px;display:flex;gap:2px}
.social__dots span{width:10px;height:10px;border-radius:50%;background:var(--white)}
.book{position:absolute;left:43px;top:798px;width:359px;height:96px;background:var(--white);text-align:center;padding-top:14px}
.book__title{font-weight:700;font-size:15.5px;line-height:17px}
.book__title .red{color:var(--red)}
.book__note{font-size:12px;line-height:14px;margin-top:6px}
</style>
</head>
<body>

<section class="hanger hanger--front">
  <svg class="hanger__art" viewBox="0 0 445 1024" width="445" height="1024">
    <defs>
      <linearGradient id="night" x1="0" y1="0" x2="0" y2="1">
        <stop offset="0" stop-color="#2b6fc4"/>
        <stop offset=".45" stop-color="#2c4c93"/>
        <stop offset="1" stop-color="#4a3550"/>
      </linearGradient>
      <linearGradient id="silk" x1="0" y1="0" x2="1" y2="1">
        <stop offset="0" stop-color="#e8e8e8"/>
        <stop offset=".5" stop-color="#ffffff"/>
        <stop offset="1" stop-color="#efefef"/>
      </linearGradient>
    </defs>
    <rect width="445" height="1024" fill="url(#silk)"/>
    <path d="M0 0H445V410Q222 500 0 410Z" fill="url(#night)" role="img" aria-label="Photo of a city skyline at dusk with lit office towers"/>
    <path d="M0 410Q222 500 445 410V440Q222 535 0 440Z" fill="var(--red)"/>
    <path d="M0 462Q222 560 445 462" fill="none" stroke="var(--red)" stroke-width="4"/>
    <circle cx="221" cy="135" r="69" fill="var(--white)"/>
    <circle cx="221" cy="135" r="59" fill="var(--stage)"/>
    <path d="M0 905Q30 890 60 885H385Q415 890 445 905V1024H0Z" fill="var(--ink)"/>
    <path d="M0 880L43 862V885L0 905Z" fill="var(--red)"/>
    <path d="M445 880L402 862V885L445 905Z" fill="var(--red)"/>
  </svg>

  <div class="logo">
    <div class="logo__name">K&amp;T</div>
    <div class="logo__sub">ELECTRIC, LLC</div>
  </div>

  <p class="abs center front-kicker">Need a Reliable Electrician?</p>
  <h1 class="abs center front-title"><span class="red">Your Local Electrical</span><br>Expert is Just Around<br>the Corner!</h1>

  <div class="perks">
    <div class="perk" style="left:18px;top:17px"><svg class="tick" viewBox="0 0 14 14"><circle cx="7" cy="7" r="7" fill="var(--red)"/><path d="M4 7.2l2 2 4-4.2" fill="none" stroke="#fff" stroke-width="1.8"/></svg>Quick Response<br>Times</div>
    <div class="perk" style="left:206px;top:17px"><svg class="tick" viewBox="0 0 14 14"><circle cx="7" cy="7" r="7" fill="var(--red)"/><path d="M4 7.2l2 2 4-4.2" fill="none" stroke="#fff" stroke-width="1.8"/></svg>Quality<br>Workmanship</div>
    <div class="perk" style="left:18px;top:74px"><svg class="tick" viewBox="0 0 14 14" style="top:-6px"><circle cx="7" cy="7" r="7" fill="var(--red)"/><path d="M4 7.2l2 2 4-4.2" fill="none" stroke="#fff" stroke-width="1.8"/></svg>Affordable Rates</div>
    <div class="perk" style="left:206px;top:74px"><svg class="tick" viewBox="0 0 14 14"><circle cx="7" cy="7" r="7" fill="var(--red)"/><path d="M4 7.2l2 2 4-4.2" fill="none" stroke="#fff" stroke-width="1.8"/></svg>Fully Licensed &amp;<br>Insured</div>
  </div>

  <div class="offer-line"></div>
  <div class="offer-pill">Special Offer:</div>
  <div class="offer-box">
    <div class="offer-pct">10<small><span>%</span><span>OFF</span></small></div>
    <div class="offer-text">YOUR FIRST SERVICE CALL!</div>
  </div>

  <div class="tear"></div>
  <div class="foot" style="left:65px;top:949px"><b>K&amp;T Electric</b></div>
  <svg class="foot-ico" style="left:43px;top:975px" viewBox="0 0 14 14"><circle cx="7" cy="7" r="7" fill="var(--red)"/><path d="M4.5 3.5l1.6 0 .6 2-1 .8a5 5 0 0 0 2.4 2.4l.8-1 2 .6v1.6c-3.5.5-7-3-6.4-6.4z" fill="#fff"/></svg>
  <div class="foot" style="left:64px;top:975px">(555) 318-4702</div>
  <svg class="foot-ico" style="left:188px;top:948px" viewBox="0 0 14 14"><circle cx="7" cy="7" r="7" fill="var(--red)"/><rect x="3.5" y="4.5" width="7" height="5" fill="none" stroke="#fff" stroke-width="1"/><path d="M3.5 4.5l3.5 3 3.5-3" fill="none" stroke="#fff" stroke-width="1"/></svg>
  <div class="foot" style="left:209px;top:948px">www.kandtelectric.example</div>
  <svg class="foot-ico" style="left:188px;top:975px" viewBox="0 0 14 14"><circle cx="7" cy="7" r="7" fill="var(--red)"/><circle cx="7" cy="7" r="3.6" fill="none" stroke="#fff" stroke-width="1"/><path d="M3.4 7h7.2M7 3.4v7.2" stroke="#fff" stroke-width=".8"/></svg>
  <div class="foot" style="left:209px;top:975px">info@kandtelectric.example</div>
</section>

<section class="hanger hanger--back">
  <svg class="hanger__art" viewBox="0 0 445 1024" width="445" height="1024">
    <defs>
      <linearGradient id="warm" x1="0" y1="0" x2="1" y2="1">
        <stop offset="0" stop-color="#cfc6b0"/>
        <stop offset=".5" stop-color="#e6d5ad"/>
        <stop offset="1" stop-color="#f1ede4"/>
      </linearGradient>
      <linearGradient id="silk2" x1="0" y1="0" x2="1" y2="1">
        <stop offset="0" stop-color="#ffffff"/>
        <stop offset=".6" stop-color="#ececec"/>
        <stop offset="1" stop-color="#f8f8f8"/>
      </linearGradient>
    </defs>
    <rect width="445" height="1024" fill="url(#silk2)"/>
    <path d="M0 0H445V208Q222 300 0 208Z" fill="url(#warm)" role="img" aria-label="Photo of glowing filament light bulbs hanging among green leaves"/>
    <path d="M0 215Q222 305 445 215V250Q222 335 0 250Z" fill="var(--red)"/>
    <path d="M0 258Q222 345 445 258" fill="none" stroke="var(--red)" stroke-width="3"/>
    <circle cx="221" cy="135" r="60" fill="var(--stage)"/>
    <path d="M0 905Q30 890 60 885H385Q415 890 445 905V1024H0Z" fill="var(--ink)"/>
    <path d="M0 880L43 862V885L0 905Z" fill="var(--red)"/>
    <path d="M445 880L402 862V885L445 905Z" fill="var(--red)"/>
  </svg>

  <h2 class="abs center back-title">Don't Let Electrical Issues<br><span class="red">Keep You in the Dark!</span></h2>
  <p class="abs center back-lede">From flickering lights to complete system upgrades, we've got all your residential electrical needs covered.</p>

  <div class="info">
    <div class="info__frame"></div>
    <div class="info__base"></div>
    <div class="info__tab">Our services</div>
    <div class="info__head"><span class="red">Why</span> Choose Us</div>

    <div class="item" style="left:0;top:38px"><svg class="tick" viewBox="0 0 14 14"><circle cx="7" cy="7" r="7" fill="var(--red)"/><path d="M4 7.2l2 2 4-4.2" fill="none" stroke="#fff" stroke-width="2"/></svg>Electrical Repairs &amp;<br>Troubleshooting</div>
    <div class="item" style="left:0;top:78px"><svg class="tick" viewBox="0 0 14 14"><circle cx="7" cy="7" r="7" fill="var(--red)"/><path d="M4 7.2l2 2 4-4.2" fill="none" stroke="#fff" stroke-width="2"/></svg>Lighting Installation &amp;<br>Upgrades</div>
    <div class="item" style="left:0;top:118px"><svg class="tick" viewBox="0 0 14 14"><circle cx="7" cy="7" r="7" fill="var(--red)"/><path d="M4 7.2l2 2 4-4.2" fill="none" stroke="#fff" stroke-width="2"/></svg>Safety Inspections &amp;<br>Code Compliance</div>
    <div class="item" style="left:0;top:159px"><svg class="tick" viewBox="0 0 14 14"><circle cx="7" cy="7" r="7" fill="var(--red)"/><path d="M4 7.2l2 2 4-4.2" fill="none" stroke="#fff" stroke-width="2"/></svg>Energy-Efficient Solutions</div>
    <div class="item" style="left:0;top:186px"><svg class="tick" viewBox="0 0 14 14"><circle cx="7" cy="7" r="7" fill="var(--red)"/><path d="M4 7.2l2 2 4-4.2" fill="none" stroke="#fff" stroke-width="2"/></svg>24/7 Emergency Services</div>

    <div class="item" style="left:206px;top:59px"><svg class="tick" viewBox="0 0 14 14"><circle cx="7" cy="7" r="7" fill="var(--red)"/><path d="M4 7.2l2 2 4-4.2" fill="none" stroke="#fff" stroke-width="2"/></svg>Friendly, Local Service</div>
    <div class="item" style="left:206px;top:88px"><svg class="tick" viewBox="0 0 14 14"><circle cx="7" cy="7" r="7" fill="var(--red)"/><path d="M4 7.2l2 2 4-4.2" fill="none" stroke="#fff" stroke-width="2"/></svg>Over 30 Years of<br>Experience</div>
    <div class="item" style="left:206px;top:131px"><svg class="tick" viewBox="0 0 14 14"><circle cx="7" cy="7" r="7" fill="var(--red)"/><path d="M4 7.2l2 2 4-4.2" fill="none" stroke="#fff" stroke-width="2"/></svg>Satisfaction<br>Guaranteed</div>
    <div class="item" style="left:206px;top:175px"><svg class="tick" viewBox="0 0 14 14"><circle cx="7" cy="7" r="7" fill="var(--red)"/><path d="M4 7.2l2 2 4-4.2" fill="none" stroke="#fff" stroke-width="2"/></svg>Upfront Pricing</div>
  </div>

  <p class="abs center call">Call Us Today: <b>(555) 318-4702</b></p>
  <p class="abs center site-label">Visit Our Website:</p>
  <p class="abs center site">www.kandtelectric.example</p>

  <div class="social">Follow Us on Social Media for More Tips and Special Offers!
    <div class="social__dots" role="img" aria-label="Chatterpage, Quibbler and Pixmosaic profiles"><span></span><span></span><span></span></div>
  </div>

  <div class="book">
    <p class="book__title">Book Your Appointment Now and Claim<br><span class="red">Your 10% Discount!</span></p>
    <p class="book__note">Offer valid for new customers on the first visit only.<br>Mention this door hanger when booking.</p>
  </div>

  <div class="tear"></div>
  <div class="foot" style="left:65px;top:949px"><b>K&amp;T Electric</b></div>
  <svg class="foot-ico" style="left:43px;top:975px" viewBox="0 0 14 14"><circle cx="7" cy="7" r="7" fill="var(--red)"/><path d="M4.5 3.5l1.6 0 .6 2-1 .8a5 5 0 0 0 2.4 2.4l.8-1 2 .6v1.6c-3.5.5-7-3-6.4-6.4z" fill="#fff"/></svg>
  <div class="foot" style="left:64px;top:975px">(555) 318-4702</div>
  <svg class="foot-ico" style="left:188px;top:948px" viewBox="0 0 14 14"><circle cx="7" cy="7" r="7" fill="var(--red)"/><rect x="3.5" y="4.5" width="7" height="5" fill="none" stroke="#fff" stroke-width="1"/><path d="M3.5 4.5l3.5 3 3.5-3" fill="none" stroke="#fff" stroke-width="1"/></svg>
  <div class="foot" style="left:209px;top:948px">www.kandtelectric.example</div>
  <svg class="foot-ico" style="left:188px;top:975px" viewBox="0 0 14 14"><circle cx="7" cy="7" r="7" fill="var(--red)"/><circle cx="7" cy="7" r="3.6" fill="none" stroke="#fff" stroke-width="1"/><path d="M3.4 7h7.2M7 3.4v7.2" stroke="#fff" stroke-width=".8"/></svg>
  <div class="foot" style="left:209px;top:975px">info@kandtelectric.example</div>
</section>

</body>
</html>
```